Barristers Chambers - Letterhead and Logo amendments

Marrowby Chambers is a barristers chambers in Thornbeck Rise, just around the corner from st. Orwins cathedral. We already have the logo and colour scheme but I think it can be improved, possibly with a better lettermark? we also have a small square version of it.
Main brand colour is: 671E75 – Purple.
Slogan: CONNECTING BARRISTERS, SOLICITORS AND OTHER PROFESSIONALS
I will attach both logos and also our current letterhead, which we made ourselves but it doesn't look professional enough.
Name of the Chambers: Marrowby Chambers
Tagline/Slogan (if any): None
Design Elements:
The logo should be simple and easy to recognize.
It should reflect the nature of the Chambers' work and be relevant to the legal industry.
Any images or graphics used should be unique, professional, and not overly complex.
The logo should be adaptable to various media, such as business cards, letterheads, and digital marketing materials.
It should be legible and easy to read, even when used at a small size.
The colour scheme should be professional and reflect the Chambers' brand identity.
Target Market(s)
Solicitors, lawyers and business clients
Industry/Entity Type
Legal

```html
<!DOCTYPE html>
<html lang="en">
<head>
<meta charset="utf-8">
<title>Marrowby Chambers – Letterhead</title>
<link rel="stylesheet" href="https://fonts.googleapis.com/css2?family=Heebo:wght@400;500&display=swap">
<style>
  :root {
    --brand-purple: #671E75;
    --ink: #3a3a3a;
    --paper: #ffffff;
    --paper-shade: #efefef;
    --backdrop: #e4e2e5;
    --mark-faint: rgba(103, 30, 117, 0.07);
  }
  * { margin: 0; padding: 0; box-sizing: border-box; }
  html, body {
    width: 1084px; height: 1200px; overflow: hidden;
    background: var(--backdrop);
    font-family: "Heebo", sans-serif;
  }
  .letterhead {
    position: absolute; left: 94px; top: 20px;
    width: 895px; height: 1160px;
    background:
      linear-gradient(to bottom, var(--paper) 0, var(--paper-shade) 385px, transparent 385px),
      linear-gradient(to bottom, transparent 385px, var(--paper) 385px, var(--paper-shade) 773px, transparent 773px),
      linear-gradient(to bottom, transparent 773px, var(--paper) 773px, var(--paper-shade) 1141px);
    box-shadow: 0 6px 18px rgba(0,0,0,0.18);
  }
  .brand {
    position: absolute; left: 54px; top: 50px;
    display: flex; align-items: center; gap: 8px;
  }
  .brand-square {
    width: 54px; height: 54px;
    border: 2px solid var(--brand-purple);
    flex: none;
  }
  .brand-name {
    color: var(--brand-purple);
    font-weight: 500; font-size: 23px; letter-spacing: 0.5px;
    text-transform: uppercase; line-height: 25px;
  }
  .brand-name span { display: block; }
  .address {
    position: absolute; left: 388px; top: 50px;
    font-style: normal; font-size: 14.5px; line-height: 19px;
    color: var(--ink);
  }
  .contacts {
    position: absolute; left: 576px; top: 48px;
    list-style: none; font-size: 14.5px; line-height: 20px; color: var(--ink);
  }
  .contacts li { display: flex; align-items: center; gap: 6px; }
  .contacts svg { width: 14px; height: 14px; flex: none; fill: var(--brand-purple); }
  .faint-mark {
    position: absolute; left: 227px; top: 379px;
    width: 440px; height: 402px;
    border: 12px solid var(--mark-faint);
    box-shadow: inset 0 0 0 4px var(--mark-faint);
    display: flex; align-items: center; justify-content: center;
  }
  .faint-mark-name {
    color: var(--mark-faint);
    font-weight: 500; font-size: 56px; line-height: 70px; letter-spacing: 1px;
    text-transform: uppercase; text-align: center;
  }
  .faint-mark-name span { display: block; }
  .footer-band {
    position: absolute; left: 0; bottom: 0;
    width: 100%; height: 19px;
    background: var(--brand-purple);
  }
</style>
</head>
<body>
  <main class="letterhead">
    <header>
      <div class="brand">
        <span class="brand-square"></span>
        <span class="brand-name"><span>Marrowby</span><span>Chambers</span></span>
      </div>
      <address class="address">
        Marrowby Chambers<br>
        Suite 1, 39 Thornbeck Rise<br>
        London EC9Z 4QX
      </address>
      <ul class="contacts">
        <li>
          <svg viewBox="0 0 24 24" aria-hidden="true"><path d="M6.6 10.8a15.1 15.1 0 0 0 6.6 6.6l2.2-2.2c.3-.3.7-.4 1-.2 1.1.4 2.3.6 3.6.6.6 0 1 .4 1 1V20c0 .6-.4 1-1 1A17 17 0 0 1 3 4c0-.6.4-1 1-1h3.5c.6 0 1 .4 1 1 0 1.3.2 2.5.6 3.6.1.3 0 .7-.2 1z"/></svg>
          01632 960482
        </li>
        <li>
          <svg viewBox="0 0 24 24" aria-hidden="true"><path d="M2 5h20v14H2zm2 2v.5l8 5 8-5V7zm0 2.8V17h16V9.8l-8 5z"/></svg>
          contact@marrowbychambers.co.uk
        </li>
        <li>
          <svg viewBox="0 0 24 24" aria-hidden="true"><path d="M12 2a10 10 0 1 0 0 20 10 10 0 0 0 0-20zm6.9 6h-2.9a15 15 0 0 0-1.3-3.9A8 8 0 0 1 18.9 8zM12 4c.8 1.2 1.5 2.5 1.9 4h-3.8c.4-1.5 1.100-2.8 1.9-4zM4.3 14a8 8 0 0 1 0-4h3.4a16 16 0 0 0 0 4zm.8 2h2.9c.3 1.4.8 2.7 1.3 3.9A8 8 0 0 1 5.1 16zM8 8H5.1a8 8 0 0 1 4.2-3.9C8.8 5.3 8.3 6.6 8 8zm4 12c-.8-1.2-1.5-2.5-1.9-4h3.8c-.4 1.5-1.1 2.8-1.9 4zm2.3-6H9.7a14 14 0 0 1 0-4h4.6a14 14 0 0 1 0 4zm.4 5.9c.5-1.2 1-2.5 1.3-3.9h2.9a8 8 0 0 1-4.2 3.9zm1.6-5.9a16 16 0 0 0 0-4h3.4a8 8 0 0 1 0 4z"/></svg>
          www.marrowbychambers.co.uk
        </li>
      </ul>
    </header>
    <div class="faint-mark" aria-hidden="true">
      <span class="faint-mark-name"><span>Marrowby</span><span>Chambers</span></span>
    </div>
    <div class="footer-band"></div>
  </main>
</body>
</html>
```